Environmental Group Website Template

We want a website template for an environmental cause. The website should have a dark content area that is transparent. The website text and icons are white.
The background is a nature scene. The background image repeats.
Industry/Entity Type
Group

```html
<!DOCTYPE html>
<html lang="en">
<head>
<meta charset="utf-8">
<title>Environmental Group Template</title>
<link href="https://fonts.googleapis.com/css2?family=Economica:wght@700&family=Pathway+Gothic+One&family=Source+Sans+3:wght@400;600&family=Fira+Sans:wght@500;600&display=swap" rel="stylesheet">
<style>
  :root {
    --sky-blue: #3497cd;
    --light-blue: #4aa8d0;
    --deep-blue: #2d89b8;
    --title-navy: #1f5e80;
    --header-dark: rgba(30, 30, 30, 0.82);
    --white: #ffffff;
    --footer-text: #555555;
    --footer-icon: #2b6aa0;
  }
  * { box-sizing: border-box; margin: 0; padding: 0; }
  html, body { width: 1116px; height: 1200px; overflow: hidden; background: #e6e6e6; }
  body { font-family: "Source Sans 3", sans-serif; color: var(--white); position: relative; }

  .hero {
    position: absolute; left: 0; top: 0; width: 1116px; height: 648px;
    background:
      radial-gradient(ellipse 260px 120px at 180px 210px, rgba(120,140,40,0.95), transparent 70%),
      radial-gradient(ellipse 420px 70px at 820px 150px, rgba(130,150,45,0.9), transparent 75%),
      radial-gradient(ellipse 140px 200px at 1060px 490px, rgba(70,110,40,0.9), transparent 75%),
      linear-gradient(180deg, #5a6a2a 0%, #7b8f3a 18%, #55677f 30%, #3e4d6e 55%, #34415f 80%, #4f6a38 92%, #6a8a30 100%);
  }
  .header {
    position: absolute; left: 0; top: 0; width: 1116px; height: 95px;
    background: var(--header-dark);
  }
  .brand { position: absolute; left: 38px; top: 28px; display: flex; align-items: center; gap: 10px; }
  .brand-mark { width: 40px; height: 40px; border-radius: 50%; background: #e89a2a; }
  .brand-name { font-family: "Source Sans 3", sans-serif; font-size: 15px; line-height: 17px; text-align: center; color: #e8e8e8; }

  .nav { position: absolute; right: 142px; top: 0; height: 95px; display: flex; align-items: center; gap: 17px; }
  .nav-item { position: relative; display: flex; align-items: center; gap: 4px; font-family: "Economica", sans-serif; font-weight: 700; font-size: 15px; letter-spacing: 0.3px; text-transform: uppercase; color: var(--white); height: 95px; }
  .nav-item svg { width: 11px; height: 11px; fill: var(--white); }
  .nav-item.is-active::after { content: ""; position: absolute; left: 0; right: 0; bottom: 0; height: 3px; background: var(--sky-blue); }
  .donate-tab { position: absolute; left: 991px; top: 0; width: 82px; height: 95px; background: var(--sky-blue); display: flex; align-items: center; justify-content: center; gap: 4px; font-family: "Economica", sans-serif; font-weight: 700; font-size: 15px; text-transform: uppercase; }
  .donate-tab svg { width: 11px; height: 11px; fill: var(--white); }

  .hero-copy { position: absolute; left: 84px; top: 330px; width: 480px; }
  .hero-title { font-family: "Pathway Gothic One", sans-serif; font-weight: 400; font-size: 44px; line-height: 46px; }
  .hero-text { margin-top: 14px; font-size: 18px; line-height: 25px; font-weight: 400; }
  .outline-btn { display: flex; align-items: center; justify-content: center; width: 192px; height: 25px; border: 2px solid var(--white); border-radius: 13px; font-family: "Source Sans 3", sans-serif; font-weight: 600; font-size: 13px; text-transform: uppercase; color: var(--white); }
  .hero .outline-btn { margin-top: 20px; }
  .slider-dots { position: absolute; top: 639px; left: 541px; display: flex; gap: 6px; }
  .slider-dots span { width: 9px; height: 9px; border: 1px solid var(--white); border-radius: 50%; }
  .slider-dots span.is-current { background: var(--white); }

  .intro { position: absolute; left: 0; top: 648px; width: 1116px; height: 206px; background: var(--sky-blue); text-align: center; box-shadow: inset 0 12px 12px -10px rgba(0,0,0,0.35); }
  .intro-title { margin-top: 30px; font-family: "Fira Sans", sans-serif; font-weight: 600; font-size: 25px; color: var(--title-navy); letter-spacing: 0.5px; }
  .intro-text { width: 1000px; margin: 16px auto 0; font-size: 13.5px; line-height: 18px; letter-spacing: -0.2px; }

  .actions { position: absolute; left: 0; top: 858px; width: 1116px; height: 291px; display: flex; }
  .action { height: 291px; text-align: center; display: flex; flex-direction: column; align-items: center; }
  .action--volunteer { width: 396px; background: var(--light-blue); }
  .action--support { width: 324px; background: var(--sky-blue); }
  .action--voice { width: 396px; background: var(--deep-blue); }
  .action-icon { margin-top: 38px; width: 70px; height: 70px; border: 2px solid var(--white); border-radius: 50%; display: flex; align-items: center; justify-content: center; }
  .action-icon svg { width: 44px; height: 44px; fill: var(--white); }
  .action-title { margin-top: 17px; font-family: "Fira Sans", sans-serif; font-weight: 500; font-size: 19px; }
  .action-text { margin-top: 10px; width: 280px; font-size: 13.5px; line-height: 18px; letter-spacing: -0.2px; }
  .action .outline-btn { margin-top: 14px; }

  .footer { position: absolute; left: 0; top: 1149px; width: 1116px; height: 51px; background: var(--white); box-shadow: inset 0 10px 10px -9px rgba(0,0,0,0.3); }
  .social { position: absolute; left: 38px; top: 19px; display: flex; gap: 7px; align-items: center; }
  .social .dot { width: 15px; height: 15px; border-radius: 50%; background: var(--footer-icon); }
  .social svg { width: 18px; height: 15px; }
  .copyright { position: absolute; right: 40px; top: 19px; font-size: 11px; color: var(--footer-text); text-transform: uppercase; }
</style>
</head>
<body>
  <section class="hero" role="img" aria-label="Photo of a calm salt marsh with green grass islands and rippling blue water">
  </section>

  <header class="header">
    <div class="brand">
      <span class="brand-mark"></span>
      <span class="brand-name">YOUR LOGO<br>HERE</span>
    </div>
    <nav class="nav">
      <span class="nav-item is-active"><svg viewBox="0 0 10 10"><path d="M5 0L0 5h1.5v5h2.5V7h2v3h2.5V5H10z"/></svg>Home</span>
      <span class="nav-item"><svg viewBox="0 0 10 10"><path d="M5 0C3 3 2 5 2 7a3 3 0 006 0c0-2-1-4-3-7z"/></svg>About</span>
      <span class="nav-item"><svg viewBox="0 0 10 10"><circle cx="2.5" cy="6.5" r="2.5"/><circle cx="7.5" cy="6.5" r="2.5"/></svg>Explore</span>
      <span class="nav-item"><svg viewBox="0 0 10 10"><path d="M6 0L2 5h3L3 10l5-6H5z"/></svg>Challenges</span>
      <span class="nav-item"><svg viewBox="0 0 10 10"><circle cx="5" cy="5" r="4.5" fill="none" stroke="#fff" stroke-width="1.2"/><circle cx="5" cy="5" r="2"/></svg>Solutions</span>
      <span class="nav-item"><svg viewBox="0 0 10 10"><path d="M0 1h10v9H0z" fill="none" stroke="#fff" stroke-width="1.2"/><path d="M0 1h10v2H0z"/></svg>Events</span>
      <span class="nav-item"><svg viewBox="0 0 10 10"><path d="M0 2h8v7H0zM8 4h2v5H8z"/></svg>News</span>
    </nav>
    <span class="donate-tab"><svg viewBox="0 0 10 10"><path d="M2 10V4h2l2-4 2 1-1 3h3v3l-2 3z"/></svg>Donate</span>
  </header>

  <div class="hero-copy">
    <h1 class="hero-title">LOREM IPSUM</h1>
    <p class="hero-text">Lorem ipsum dolor sit amet, consectetuer adipiscing elit, sed diam nonummy nibh euismod tincidunt ut laoreet dolore magna aliquam erat volutpat.</p>
    <span class="outline-btn">Learn More</span>
  </div>
  <div class="slider-dots"><span class="is-current"></span><span></span><span></span><span></span></div>

  <section class="intro">
    <h2 class="intro-title">LOREM IPSUM</h2>
    <p class="intro-text">Lorem ipsum dolor sit amet, consectetuer adipiscing elit, sed diam nonummy nibh euismod tincidunt ut laoreet dolore magna aliquam erat volutpat. Ut wisi enim ad minim veniam, quis nostrud exerci tation ullamcorper suscipit lobortis nisl ut aliquip ex ea commodo consequat. Duis autem vel eum iriure dolor in hendrerit in vulputate velit esse molestie consequat, vel illum dolore eu feugiat nulla facilisis at vero eros et accumsan et iusto odio dignissim qui blandit praesent luptatum zzril delenit augue duis dolore te feugait nulla facilisi. Nam liber tempor cum soluta nobis eleifend option congue nihil imperdiet doming id quod mazim placerat facer possim assum. Typi non habent claritatem insitam; est usus legentis in iis qui facit eorum claritatem. Investigationes demonstraverunt lectores legere me lius quod ii legunt saepius.</p>
  </section>

  <section class="actions">
    <article class="action action--volunteer">
      <div class="action-icon"><svg viewBox="0 0 44 44"><circle cx="22" cy="10" r="5"/><path d="M6 8l5-2 7 14h8l7-14 5 2-9 18v14h-14V26z"/></svg></div>
      <h3 class="action-title">Volunteer</h3>
      <p class="action-text">Lorem ipsum dolor sit amet, consectetuer adipis elit, sed diam nonummy nibh euismod tincidunt laoreet dolore magna aliquam erat volutpat.</p>
      <span class="outline-btn">Learn More</span>
    </article>
    <article class="action action--support">
      <div class="action-icon"><svg viewBox="0 0 44 44"><rect x="2" y="6" width="40" height="14" rx="7"/><path d="M18 18h4v8l8 2v10l-4 4h-8l-6-8 2-2 4 3z"/></svg></div>
      <h3 class="action-title">Support Our Work</h3>
      <p class="action-text">Lorem ipsum dolor sit amet, consectetuer adipis elit, sed diam nonummy nibh euismod tincidunt laoreet dolore magna aliquam erat volutpat.</p>
      <span class="outline-btn">Learn More</span>
    </article>
    <article class="action action--voice">
      <div class="action-icon"><svg viewBox="0 0 44 44"><rect x="20" y="2" width="20" height="12"/><rect x="4" y="10" width="14" height="10"/><circle cx="14" cy="28" r="5"/><circle cx="30" cy="28" r="5"/><circle cx="22" cy="24" r="5"/><path d="M4 42c0-6 4-9 10-9s10 3 10 9zM20 42c0-6 4-9 10-9s10 3 10 9z"/></svg></div>
      <h3 class="action-title">Make Your Voice Heard</h3>
      <p class="action-text">Lorem ipsum dolor sit amet, consectetuer adipis elit, sed diam nonummy nibh euismod tincidunt laoreet dolore magna aliquam erat volutpat.</p>
      <span class="outline-btn">Learn More</span>
    </article>
  </section>

  <footer class="footer">
    <div class="social">
      <svg viewBox="0 0 18 14"><rect x="0.5" y="0.5" width="17" height="13" fill="none" stroke="#777"/><path d="M0.5 0.5L9 8l8.5-7.5" fill="none" stroke="#777"/></svg>
      <span class="dot"></span><span class="dot"></span><span class="dot"></span><span class="dot"></span><span class="dot"></span>
      <svg viewBox="0 0 15 15"><circle cx="2.5" cy="12.5" r="2" fill="#555"/><path d="M1 7a7 7 0 017 7M1 2a12 12 0 0112 12" fill="none" stroke="#555" stroke-width="2"/></svg>
    </div>
    <p class="copyright">© 2015 Company Name. All rights reserved</p>
  </footer>
</body>
</html>
```